Vesk Architecture

We are a architectural design and build company working between scales 1/1000 to 1/1 we want people to understand our difference from our design experience and quality.we build hotels restourants and office spaces.Our company name is Vesk architecture to mind sustainability.

We want to write our adress phone and work spesifications on the card and we want our logo as backround.

Ps:you could find the logo adress and phone box numbers from the web:www.veskmimarlik-ornek.com

Target Market(s)

Who looks for experts.

Industry/Entity Type

Architecture

Requirements
Must have
• Design is over everything.
Should not have
• we don want it to be colorfull

```html
<!DOCTYPE html>
<html lang="tr">
<head>
<meta charset="utf-8">
<title>Vesk Mimarlık – Business Card</title>
<link rel="stylesheet" href="https://fonts.googleapis.com/css2?family=Arimo:wght@400;700&display=swap">
<style>
  :root {
    --ink: #1e1e1e;
    --ink-soft: #2f2f2f;
    --mark-faint: #d4d4d4;
    --card-edge: #3a3a3a;
    --paper: #ffffff;
  }
  * { margin: 0; padding: 0; box-sizing: border-box; }
  html, body {
    width: 1200px;
    height: 431px;
    overflow: hidden;
    background: var(--paper);
  }
  body {
    position: relative;
    font-family: "Arimo", Arial, sans-serif;
    color: var(--ink);
  }
  .card {
    position: absolute;
    top: 27px;
    height: 322px;
    background: var(--paper);
    border: 1.5px solid var(--card-edge);
    overflow: hidden;
  }
  .card--front { left: 4px; width: 585px; }
  .card--back { left: 627px; width: 551px; }

  .wordmark {
    position: absolute;
    left: 0;
    right: 0;
    text-align: center;
    font-weight: 400;
    color: var(--ink);
    line-height: 1;
  }
  .wordmark__name {
    display: block;
    font-size: 118px;
    letter-spacing: 2px;
  }
  .wordmark__sub {
    display: block;
    margin-top: 24px;
    font-size: 29px;
    letter-spacing: 7px;
  }
  .card--front .wordmark { top: 68px; }

  .card--back .wordmark {
    top: 20px;
    left: 16px;
    right: auto;
    width: 270px;
    text-align: left;
    color: var(--mark-faint);
  }
  .card--back .wordmark__name { font-size: 118px; letter-spacing: 0; }
  .card--back .wordmark__sub { margin-top: -14px; font-size: 30px; letter-spacing: 8px; }

  .contact {
    position: absolute;
    right: 12px;
    bottom: 84px;
    width: 290px;
    text-align: right;
    font-style: normal;
    transform: rotate(-20deg);
    transform-origin: right bottom;
    color: var(--ink-soft);
  }
  .contact__name { font-size: 19px; font-weight: 400; }
  .contact__role {
    font-size: 12px;
    font-weight: 700;
    letter-spacing: 4px;
    margin: 2px 24px 16px 0;
  }
  .contact__line { font-size: 12px; line-height: 1.35; }

  .side-label {
    position: absolute;
    top: 398px;
    width: 200px;
    text-align: center;
    font-size: 18px;
    letter-spacing: 0.5px;
    color: var(--ink);
  }
  .side-label--front { left: 183px; }
  .side-label--back { left: 804px; }
</style>
</head>
<body>
  <section class="card card--front" aria-label="Card front">
    <div class="wordmark">
      <span class="wordmark__name">vesk</span>
      <span class="wordmark__sub">MİMARLIK</span>
    </div>
  </section>

  <section class="card card--back" aria-label="Card back">
    <div class="wordmark" aria-hidden="true">
      <span class="wordmark__name">vesk</span>
      <span class="wordmark__sub">MİMARLIK</span>
    </div>
    <address class="contact">
      <p class="contact__name">Selim Aras TUNALI</p>
      <p class="contact__role">Mimar</p>
      <p class="contact__line">Kuyulu Mah. Lale Cad. Ceren Apt.</p>
      <p class="contact__line">No : 7 Yalıboyu / ISTANBUL</p>
      <p class="contact__line">t. 0216 555 01 47</p>
      <p class="contact__line">f. 0216 555 01 48</p>
      <p class="contact__line">e. vesk.ornek@posta-ornek.com</p>
    </address>
  </section>

  <p class="side-label side-label--front">FRONT</p>
  <p class="side-label side-label--back">BACK</p>
</body>
</html>
```